Tobin's Jewelry Studio Needs a Moving Location Flyer

We need a flyer to inform our customers of our location moving. We will be moving to our city's downtown which is only 1 mile away from our current address. We will be having a moving sale ( Up to 80% off). The sale starts Sept. 8th Our business creates, sells, and repairs fine jewelry. Dimensions are 5"x8"

Target Market(s)

Women ages 25-55

Industry/Entity Type

Jewelry

Colors
85abd2
cfdeed

Requirements
Must have
• Our logo
• Mention of the sale
• Our current address
• 4785 Cresthaven Blvd.
• Dunmore, Ca 94318
• (415)826-3319
Nice to have
• Mention that we're relocating to downtown Dunmore (new location opening Nov. 1st.)

```html
<!DOCTYPE html>
<html lang="en">
<head>
<meta charset="utf-8">
<title>Tobin's Jewelry Studio – Moving Sale</title>
<link rel="stylesheet" href="https://fonts.googleapis.com/css2?family=Arimo:wght@400;700&display=swap">
<style>
  :root {
    --ink-navy: #2f5bb0;
    --sky-blue: #2e8ee6;
    --band-blue: #3399ec;
    --map-grey: #dfe4ea;
    --map-light: #f2f4f7;
    --logo-pale: #cfe3ed;
    --ink-dark: #1a1a1a;
    --white: #ffffff;
  }
  * { margin: 0; padding: 0; box-sizing: border-box; }
  html, body { width: 1200px; height: 751px; overflow: hidden; background: var(--white); }
  .flyer {
    position: relative;
    width: 1200px;
    height: 751px;
    font-family: "Arimo", Arial, sans-serif;
    background: var(--white);
    overflow: hidden;
  }
  .map-area {
    position: absolute;
    left: 0; top: 0;
    width: 1200px; height: 593px;
    background:
      radial-gradient(ellipse 520px 300px at 640px 220px, var(--map-grey), transparent 75%),
      radial-gradient(ellipse 420px 260px at 950px 230px, var(--map-light), transparent 80%),
      linear-gradient(180deg, var(--map-light) 0%, var(--white) 100%);
  }
  .move-arrow { position: absolute; left: 0; top: 0; }
  .relocation-line {
    position: absolute;
    top: 282px; left: 0; width: 1250px;
    text-align: center;
    color: var(--ink-navy);
    font-weight: 700;
    font-size: 21px;
    white-space: nowrap;
  }
  .relocation-line .city { font-size: 38px; }
  .sale-date {
    position: absolute;
    top: 388px; left: 0; width: 1200px;
    text-align: center;
    color: var(--sky-blue);
    font-weight: 700;
    font-size: 34px;
  }
  .sale-offer {
    position: absolute;
    top: 444px; left: 0; width: 1200px;
    text-align: center;
    color: var(--sky-blue);
    font-weight: 700;
    font-size: 28px;
    line-height: 38px;
  }
  .business-line {
    position: absolute;
    top: 537px; left: 0; width: 1200px;
    text-align: center;
    color: var(--sky-blue);
    font-weight: 700;
    font-size: 21px;
  }
  .contact-band {
    position: absolute;
    left: 0; top: 593px;
    width: 1200px; height: 158px;
    background: var(--band-blue);
  }
  .brand {
    position: absolute;
    left: 155px; top: 78px;
    width: 420px;
    height: 0;
  }
  .brand-rule {
    position: absolute;
    left: 0; top: 0;
    width: 420px; height: 2px;
    background: var(--ink-dark);
  }
  .brand-mark {
    position: absolute;
    left: 55px; top: -42px;
    width: 84px; height: 84px;
    border-radius: 50%;
    background: var(--logo-pale);
    border: 2px solid var(--white);
  }
  .brand-name {
    position: absolute;
    left: 155px; top: -12px;
    padding: 0 8px;
    background: var(--band-blue);
    color: var(--ink-dark);
    font-size: 19px;
    font-weight: 400;
    white-space: nowrap;
  }
  .address {
    position: absolute;
    left: 608px; top: 48px;
    color: var(--ink-dark);
    font-size: 23px;
  }
  .phone {
    position: absolute;
    left: 606px; top: 84px;
    display: flex;
    align-items: center;
    gap: 8px;
    color: var(--ink-dark);
    font-size: 23px;
  }
</style>
</head>
<body>
<div class="flyer">
  <div class="map-area" role="img" aria-label="Faded street map of the city showing the downtown area and neighbouring towns"></div>

  <svg class="move-arrow" width="1200" height="593" viewBox="0 0 1200 593" aria-hidden="true">
    <path d="M358 212 C 390 130, 500 95, 560 150 C 590 180, 598 215, 596 238 L 572 238 C 574 215, 566 190, 545 172 C 495 130, 410 140, 358 212 Z" fill="#3a97e8"/>
    <path d="M548 234 L 628 234 L 596 276 Z" fill="#3a97e8"/>
  </svg>

  <p class="relocation-line">we're relocating to downtown <span class="city">Dunmore</span> (new location opening Nov. 1st.)</p>
  <h1 class="sale-date">The sale starts Sept. 8th</h1>
  <p class="sale-offer">We will be having a<br>moving sale (Up to 80% off)</p>
  <p class="business-line">Our business tcreates, sells, and repairs fine jewelry.</p>

  <footer class="contact-band">
    <div class="brand">
      <div class="brand-rule"></div>
      <div class="brand-mark"></div>
      <span class="brand-name">Tobin's Jewelry Studio</span>
    </div>
    <p class="address">4785 Cresthaven Blvd., Dunmore, Ca 94318</p>
    <p class="phone">
      <svg width="28" height="28" viewBox="0 0 28 28" aria-hidden="true">
        <circle cx="14" cy="14" r="12.5" fill="none" stroke="#1a1a1a" stroke-width="2"/>
        <path d="M9 7.5 L12 7 L13.5 11 L11.5 12.5 C12.5 14.8 13.6 15.9 15.6 16.8 L17 14.8 L21 16.2 L20.5 19.3 C15 20 8 13 9 7.5 Z" fill="#1a1a1a"/>
      </svg>
      (415)826-3319
    </p>
  </footer>
</div>
</body>
</html>
```